Tri-Fold Brochure for Christian Author and Speaker

Loralee Pendergast is an inspirational author and speaker, sharing her testimony and encouraging others in their walk with Christ. A gifted writer, her work has been featured on Gently Radiant, Steadfast Musings, and Hymns & Teacups Journal (Fall 2011).

Loralee ‘s first book, Leaving the Lantern Room: Unmasking Hidden Snares in Ordinary Living, is an informative memoir and Bible study, recounting her journey from committed Christian to witch, medium, and ghost hunter for eight years until restored to faith in Jesus Christ. She was a contributing author to Walking Past the Shadow: A Candid Study of Mysticism by One-Time Seekers by Doug Pemberlin and a consultant for the novel The Orphan of Halvering Ridge by Marlowe Prize Winning Author, Glenna Whitcombe.

Loralee’s second book, An Insider’s Guide to Spiritual Warfare: 20 Battle-Tested Strategies from Behind Enemy Lines, will be published by Harrowgate Press for Fall 2014.

Loralee is a wife and mother. She enjoys writing, spending time with her family, taking long walks, listening to music of all kinds, and experiencing God’s daily gift called life.

You can read more about Loralee and see the look and feel we are going for at www.loraleependergast.example

The brochure is to be used as a promotional tool to gain Loralee speaking engagements. You can see the topics she covers at http://www.loraleependergast.example/speaking-engagements/.

More info can be found at: https://www.facebook.com/AuthorLoraleePendergast
https://www.facebook.com/WMUCX
https://www.facebook.com/LeavingtheLanternRoom
https://www.facebook.com/TallOakOutreach
http://www.talloakoutreach.example

I have uploaded 3 headshots, book covers for both of Loralee's books and the design layout in .EPS format from Quickleaflet.example where I will be getting printing done.

3 more days till the contest ends get your final designs in.

Reason: I'm extending this as I am tied up at a leadership conference and will not be able to give this the attention it deserves till the weekend.

Target Market(s)

Churches and women's groups. Loralee's current audience skews heavy to women on a 70/30 ratio.

Industry/Entity Type

Christian

Requirements
Must have
• Headshot I have uploaded 3
Quotes from previous speaking engagements you can find those at http://www.loraleependergast.example/speaking-engagements/

```html
<!DOCTYPE html>
<html lang="en">
<head>
<meta charset="utf-8">
<title>Loralee Pendergast – Speaker Brochure</title>
<link rel="stylesheet" href="https://fonts.googleapis.com/css2?family=Mulish:wght@300;400;700;800&display=swap">
<style>
  :root {
    --berry: #a8275f;
    --berry-deep: #8e1f4f;
    --pink: #f4c3d7;
    --pink-soft: #fbe4ee;
    --blush: #fdf1f6;
    --ink: #6b3450;
    --white: #ffffff;
  }
  * { box-sizing: border-box; margin: 0; padding: 0; }
  html, body { width: 846px; height: 1200px; overflow: hidden; }
  body {
    position: relative;
    font-family: "Mulish", Arial, sans-serif;
    color: var(--ink);
    background: var(--white);
  }
  .spread { position: absolute; left: 0; width: 846px; height: 600px; overflow: hidden; }
  .spread--outside { top: 0; background: radial-gradient(circle at 60% 20%, var(--blush), var(--pink) 80%); }
  .spread--inside { top: 600px; background: radial-gradient(circle at 50% 40%, var(--white), var(--pink-soft) 55%, var(--pink) 100%); }
  .edge-strip { position: absolute; left: 0; top: 0; width: 12px; height: 600px; background: var(--berry); }
  .foot-band { position: absolute; left: 178px; right: 0; height: 12px; background: var(--berry); }
  .spread--outside .foot-band { top: 586px; }
  .spread--inside .foot-band { bottom: 0; }
  .abs { position: absolute; }

  /* Testimonial panel */
  .speaker-photo {
    left: 12px; top: 0; width: 308px; height: 586px;
    background: linear-gradient(160deg, #f3d3df 0%, #c98aa3 45%, #6d3c4d 100%);
  }
  .title-band {
    left: 12px; top: 50px; width: 293px; height: 82px;
    background: var(--berry); color: var(--white);
    font-weight: 300; font-size: 19px; line-height: 22px;
    padding: 13px 0 0 18px;
  }
  .panel-signature {
    left: 30px; top: 535px; color: var(--white);
    font-size: 20px; font-weight: 300; letter-spacing: .5px;
  }
  .testimonials { left: 327px; top: 22px; width: 222px; font-size: 8.6px; line-height: 12.4px; }
  .testimonials p { margin-bottom: 8px; }
  .testimonials .who { text-align: right; color: var(--berry); font-weight: 700; font-size: 9.5px; margin-bottom: 0; }
  .testimonials .role { text-align: right; color: var(--berry); font-weight: 700; font-size: 7.4px; margin-bottom: 14px; }

  /* Books panel */
  .books-head { left: 565px; top: 94px; width: 281px; text-align: center; font-weight: 300; }
  .books-head .kicker { color: var(--white); font-size: 16px; }
  .books-head .name { color: var(--berry); font-size: 22px; }
  .book { left: 645px; width: 120px; box-shadow: 4px 6px 10px rgba(80,20,45,.35); }
  .book--one { top: 147px; height: 188px; background: linear-gradient(180deg, #e8e8ea, #f7f5f4 55%, #cfc8c8); }
  .book--two { top: 360px; height: 172px; background: linear-gradient(180deg, #1e1c20, #3a2c30 70%, #5c1d22); }
  .site { font-size: 13px; color: var(--berry-deep); letter-spacing: .3px; }
  .site b { font-weight: 700; }
  .books-site { left: 565px; top: 560px; width: 281px; text-align: center; }

  /* Inside: about panel */
  .stage-photo {
    left: 60px; top: 48px; width: 166px; height: 153px;
    border: 4px solid var(--pink); outline: 1px solid #e6a9c1;
    background: linear-gradient(180deg, #e9e3da, #b59587 60%, #7e5a52);
  }
  .about { left: 30px; top: 222px; width: 250px; font-size: 9.4px; line-height: 15px; font-weight: 300; }
  .topics-label {
    left: 30px; top: 346px; width: 120px; font-size: 9.5px; color: var(--berry);
    border-bottom: 1px solid var(--berry); padding-bottom: 2px;
  }
  .topics { left: 30px; top: 372px; list-style: none; }
  .topics li { color: var(--berry); font-weight: 800; font-size: 14px; line-height: 16px; margin-bottom: 12px; padding-left: 12px; position: relative; }
  .topics li::before { content: "•"; position: absolute; left: 0; font-weight: 400; }
  .topics small { display: block; font-size: 9.5px; line-height: 11px; }

  /* Inside: request panel */
  .request { left: 300px; top: 324px; width: 260px; text-align: center; }
  .request .lead { font-size: 10px; font-weight: 300; }
  .request .mark { color: var(--berry); font-size: 22px; font-weight: 300; margin: 10px 0 12px; }
  .request .ask { font-size: 10.5px; line-height: 15px; font-weight: 300; }
  .request .phone { color: var(--berry); font-size: 19px; margin: 17px 0 12px; }
  .request .thanks { font-size: 8px; font-weight: 300; }
  .request hr { width: 170px; margin: 24px auto 16px; border: 0; border-top: 1px solid #d9a3ba; }

  /* Inside: cover panel */
  .cover-flower { left: 560px; top: 90px; width: 286px; height: 380px; background: radial-gradient(ellipse at 55% 45%, #fbdfea, rgba(244,195,215,0) 70%); }
  .cover-name { left: 560px; top: 66px; width: 286px; text-align: center; color: var(--berry); font-size: 27px; font-weight: 300; line-height: 30px; }
  .cover-photo { left: 583px; top: 132px; width: 230px; height: 330px; background: linear-gradient(180deg, #f6d9e4, #b68e98 45%, #4b3032); }
  .roles { left: 640px; top: 504px; width: 126px; text-align: center; font-size: 14px; letter-spacing: 6px; color: var(--berry-deep); font-weight: 300; }
  .roles hr { border: 0; border-top: 1px dashed var(--berry); margin: 4px 0 6px; }
  .cover-site { left: 560px; top: 562px; width: 286px; text-align: center; }
</style>
</head>
<body>

<section class="spread spread--outside">
  <div class="edge-strip"></div>
  <div class="abs speaker-photo" role="img" aria-label="Photo of Loralee Pendergast smiling beside a weathered fence"></div>
  <h2 class="abs title-band">What's Loralee Like<br>as a Speaker?</h2>
  <div class="abs panel-signature">Loralee Pendergast</div>

  <div class="abs testimonials">
    <p>The Women's Ministry at Willowmere Church in Ashbourne, MI invited Loralee Pendergast to speak at our Mother or Daughter Banquet earlier this month. I am so glad she accepted! We couldn't have chosen a speaker to fit in better than Loralee. She took our theme, "Instruments", and incorporated that into her speaking time with us. She used life examples and spoke directly into the hearts of the women and girls that attended our banquet. She even took time to speak to my teen aged daughters after the banquet as to why they should stay away from the paranormal. I highly recommend Loralee as a speaker and we hope to have her back at Willowmere Church in the near future!</p>
    <p class="who">Marjorie Ellstrand</p>
    <p class="role">Willowmere Community Church Women's Ministry</p>
    <p>"Loralee came to our Hymns and Teacups Night and shared her story, it was amazing! I've never seen women so riveted by a speaker! If you are in a position to bring Loralee to your church/event...do it!"</p>
    <p class="who">Dana Whitlow</p>
    <p class="role">Hymns and Teacups Women's Ministry Events</p>
    <p>"I was honored and delighted to have Loralee Pendergast be one of our speakers in the "Harmony Crossroads Seminar Tent" at Harmony Christian Music Festival in Larkport, Michigan (one of the nation's top 10 Christian music festivals). Loralee has a unique testimony and style of speaking that keeps people, young and old, engaged into the heart of her message. Her stories of involvement in the occult and her conclusion of how God rescued her from these traps, answers many of the questions that people often have, but are afraid to ask when dealing with the "supernatural". If you are looking for a great speaker with a testimony that is relevant in today's culture of "curiosity in the supernatural", I highly recommend Loralee Pendergast to be on the top of your list of considerations."</p>
    <p class="who">Grant Holloway</p>
    <p class="role">Harmony Crossroads Seminar Tent, Coordinator</p>
  </div>

  <div class="abs books-head">
    <div class="kicker">Books by</div>
    <div class="name">Loralee Pendergast</div>
  </div>
  <div class="abs book book--one" role="img" aria-label="Book cover: Leaving the Lantern Room by Loralee Pendergast"></div>
  <div class="abs book book--two" role="img" aria-label="Book cover: Walking Past the Shadow compiled by Doug Pemberlin"></div>
  <div class="abs site books-site">www.<b>loraleependergast</b>.example</div>
  <div class="foot-band"></div>
</section>

<section class="spread spread--inside">
  <div class="edge-strip"></div>
  <div class="abs stage-photo" role="img" aria-label="Loralee Pendergast speaking into a microphone at an event"></div>
  <p class="abs about">As a speaker, Loralee Pendergast shares from her own life lessons and as a Biblical Counselor, encouraging others toward a deeper walk with God. Loralee offers sound, heartfelt, and practical biblical advice on issues relevant to the 21st Century Christian</p>
  <div class="abs topics-label">Speaking Topics Include:</div>
  <ul class="abs topics">
    <li>Christians and the Occult</li>
    <li>Homelessness<small>(with Reid Pendergast)</small></li>
    <li>Human Trafficking</li>
    <li>Marriage Restoration<small>(with Reid Pendergast)</small></li>
    <li>Prayer as a Lifestyle</li>
    <li>Spiritual Warfare</li>
  </ul>

  <div class="abs request">
    <p class="lead">To request</p>
    <p class="mark">Loralee Pendergast</p>
    <p class="ask">as a speaker for your church, meeting,<br>or event please call at:</p>
    <p class="phone">(000) 123 456 789</p>
    <p class="thanks">We look forward to hearing from you</p>
    <hr>
    <p class="site">www.<b>loraleependergast</b>.example</p>
  </div>

  <div class="abs cover-flower" role="img" aria-label="Soft pale pink lotus flower"></div>
  <div class="abs cover-name">Loralee<br>Pendergast</div>
  <div class="abs cover-photo" role="img" aria-label="Portrait of Loralee Pendergast with arms crossed"></div>
  <div class="abs roles">AUTHOR<hr>SPEAKER</div>
  <div class="abs site cover-site">www.<b>loraleependergast</b>.example</div>
  <div class="foot-band"></div>
</section>

</body>
</html>
```